Business Card & Stationary Design Project

We are looking for some creative direction for business cards and our stationary.

We are a global logistics firm that has recently changed its name to Marwick Global Logistics and we have a new website due out tomorrow (www.marwick.com.au).

The colours of the company are rich navy tones, I would like to have business cards that fit together to make one picture on the back (possibly an old map of the world??), and the front to be modern contemporary looking.

But I am open to suggestions, so just incorporate our new logo and get going!
Updates

Hi Everyone,

Thank you for all of your designs so far and the time you have put into it.

I have asked many of you for amendments to see if we can get a final product, so with this in mind I am extending the deadline by a few days.

Good luck and thank you once again.

Please message me direct if you need any clarification.

Kind Regards
Tobias

Reason: As outlined the extra 3 days is for amendments and changes to the current submissions. Thanks Tobias

Industry/Entity Type

Business

```html
<!DOCTYPE html>
<html lang="en">
<head>
<meta charset="utf-8">
<title>Marwick Global Logistics – Stationery</title>
<link href="https://fonts.googleapis.com/css2?family=Open+Sans:wght@400;600&display=swap" rel="stylesheet">
<style>
  :root {
    --backdrop: #e9e6df;
    --navy: #1f2b8f;
    --ink: #1c1c24;
    --sky: #6cb7ee;
    --band-deep: #3b4fd6;
    --band-light: #dfe4fb;
    --faint-globe: #e4e4f3;
    --tagline: #4a4fa8;
    --paper: #ffffff;
  }
  * { box-sizing: border-box; margin: 0; padding: 0; }
  html, body { width: 1200px; height: 1000px; overflow: hidden; }
  body {
    background: var(--backdrop);
    position: relative;
    font-family: "Open Sans", Arial, sans-serif;
    color: var(--ink);
  }
  .sheet { position: absolute; overflow: hidden; background: var(--paper); }

  /* Company name: plain text with a square marker */
  .brand { position: absolute; display: flex; align-items: center; gap: 8px; color: var(--navy); white-space: nowrap; }
  .brand-name { font-family: "Open Sans", Arial, sans-serif; font-weight: 600; line-height: 1; }
  .brand-mark { background: var(--navy); flex: none; }

  .band {
    position: absolute; left: 0; right: 0;
    background: linear-gradient(90deg, var(--band-deep) 0%, #9fb0f2 30%, var(--band-light) 50%, #9fb0f2 70%, var(--band-deep) 100%);
  }
  .contact { position: absolute; display: flex; align-items: center; gap: 5px; white-space: nowrap; }
  .contact svg { width: 9px; height: 9px; flex: none; }

  /* Card front */
  .card-front { left: 168px; top: 258px; width: 300px; height: 175px; background: var(--sky); }
  .card-front .band.top { top: 0; height: 10px; }
  .card-front .band.bottom { bottom: 0; height: 12px; }
  .card-front .shade { position: absolute; left: 0; right: 0; bottom: 12px; height: 5px; background: #4d7fae; }
  .card-front .brand { left: 42px; top: 64px; }
  .card-front .brand-name { font-size: 15px; }
  .card-front .brand-mark { width: 34px; height: 34px; }
  .card-front .contact { font-size: 9px; top: 144px; }

  /* Card back */
  .card-back { left: 168px; top: 488px; width: 300px; height: 176px; }
  .card-back .faint-globe { position: absolute; left: -70px; top: -10px; width: 140px; height: 140px; border-radius: 50%; background: var(--faint-globe); }
  .card-back .brand { right: 10px; top: 14px; gap: 5px; }
  .card-back .brand-name { font-size: 9px; }
  .card-back .brand-mark { width: 18px; height: 18px; }
  .card-back .holder { position: absolute; left: 10px; top: 66px; font-variant: small-caps; }
  .card-back .holder-name { font-size: 13px; }
  .card-back .holder-role { font-size: 9px; }
  .card-back .band { top: 124px; height: 52px; background: linear-gradient(180deg, #c5cdf3 0%, #5d6fe0 30%, var(--band-deep) 60%, var(--band-light) 100%); }
  .card-back .contact { font-size: 9px; }
  .card-back .contact.address { font-size: 10px; font-variant: small-caps; }

  /* Letterhead */
  .letterhead { left: 533px; top: 113px; width: 530px; height: 775px; }
  .letterhead .faint-globe { position: absolute; left: -40px; top: 398px; width: 400px; height: 420px; border-radius: 50%; background: var(--faint-globe); }
  .letterhead .contact { font-size: 8px; }
  .letterhead .contact svg { width: 8px; height: 8px; }
  .letterhead .brand { right: 34px; top: 44px; }
  .letterhead .brand-name { font-size: 14px; }
  .letterhead .brand-mark { width: 30px; height: 30px; }
  .letterhead .rule { position: absolute; left: 0; top: 104px; width: 423px; height: 4px; border-radius: 2px; background: linear-gradient(90deg, #9aa6ee, var(--band-deep) 40%, #8d9ce8 80%, #d7dcf6); }
  .letterhead .tagline { position: absolute; left: 98px; top: 736px; font-size: 17px; letter-spacing: 0.3em; color: var(--tagline); }
</style>
</head>
<body>

<!-- Card front -->
<section class="sheet card-front">
  <div class="band top"></div>
  <div class="brand">
    <span class="brand-mark"></span>
    <span class="brand-name">Marwick Global Logistics</span>
  </div>
  <div class="contact" style="left:26px">
    <svg viewBox="0 0 10 10"><circle cx="5" cy="5" r="4.5" fill="#222"/><text x="5" y="7.3" font-size="6.5" text-anchor="middle" fill="#fff" font-family="Arial">@</text></svg>
    tobias@marwick.com.au
  </div>
  <div class="contact" style="left:166px">
    <svg viewBox="0 0 10 10"><circle cx="5" cy="5" r="4.5" fill="#222"/><circle cx="5" cy="5" r="2.5" fill="none" stroke="#fff" stroke-width="0.8"/></svg>
    www.marwick.com.au
  </div>
  <div class="shade"></div>
  <div class="band bottom"></div>
</section>

<!-- Card back -->
<section class="sheet card-back">
  <div class="faint-globe" role="img" aria-label="Faint globe decoration"></div>
  <div class="brand">
    <span class="brand-mark"></span>
    <span class="brand-name">Marwick Global Logistics</span>
  </div>
  <div class="holder">
    <div class="holder-name">Full Name</div>
    <div class="holder-role">Position</div>
  </div>
  <div class="band"></div>
  <div class="contact" style="left:12px; top:132px">
    <svg viewBox="0 0 10 10"><path d="M2 1l2 2-1 1.5c.6 1.2 1.4 2 2.5 2.5L7 6l2 2-1.5 1.5C4.5 9 1 5.5.5 2.5z" fill="#222"/></svg>
    02 8417 2260
  </div>
  <div class="contact" style="left:120px; top:132px">
    <svg viewBox="0 0 10 10"><rect x="2.5" y="0.5" width="5" height="9" rx="1" fill="#222"/><rect x="3.5" y="1.8" width="3" height="5" fill="#fff"/></svg>
    0400815362
  </div>
  <div class="contact" style="left:222px; top:132px">
    <svg viewBox="0 0 10 10"><rect x="1" y="3" width="8" height="6" rx="1" fill="#222"/><rect x="3" y="1" width="4" height="3" fill="#222"/><rect x="3" y="5" width="4" height="1" fill="#fff"/></svg>
    029471 3385
  </div>
  <div class="contact address" style="left:34px; top:152px">
    <svg viewBox="0 0 10 10"><path d="M5 .5a3.5 3.5 0 0 1 3.5 3.5C8.5 6.5 5 9.5 5 9.5S1.5 6.5 1.5 4A3.5 3.5 0 0 1 5 .5z" fill="#222"/><circle cx="5" cy="4" r="1.3" fill="#fff"/></svg>
    58 Harbour Lane Pyrmont NSW 2009
  </div>
</section>

<!-- Letterhead -->
<section class="sheet letterhead">
  <div class="faint-globe" role="img" aria-label="Faint globe decoration"></div>
  <div class="contact" style="left:29px; top:52px">
    <svg viewBox="0 0 10 10"><path d="M2 1l2 2-1 1.5c.6 1.2 1.4 2 2.5 2.5L7 6l2 2-1.5 1.5C4.5 9 1 5.5.5 2.5z" fill="#222"/></svg>
    02 8417 2260
  </div>
  <div class="contact" style="left:29px; top:68px">
    <svg viewBox="0 0 10 10"><rect x="1" y="3" width="8" height="6" rx="1" fill="#222"/><rect x="3" y="1" width="4" height="3" fill="#222"/><rect x="3" y="5" width="4" height="1" fill="#fff"/></svg>
    029471 3385
  </div>
  <div class="contact" style="left:29px; top:84px">
    <svg viewBox="0 0 10 10"><path d="M5 .5a3.5 3.5 0 0 1 3.5 3.5C8.5 6.5 5 9.5 5 9.5S1.5 6.5 1.5 4A3.5 3.5 0 0 1 5 .5z" fill="#222"/><circle cx="5" cy="4" r="1.3" fill="#fff"/></svg>
    58 Harbour Lane Pyrmont NSW 2009
  </div>
  <div class="contact" style="left:133px; top:52px">
    <svg viewBox="0 0 10 10"><circle cx="5" cy="5" r="4.5" fill="#222"/><text x="5" y="7.3" font-size="6.5" text-anchor="middle" fill="#fff" font-family="Arial">@</text></svg>
    tobias@marwick.com.au
  </div>
  <div class="contact" style="left:133px; top:68px">
    <svg viewBox="0 0 10 10"><circle cx="5" cy="5" r="4.5" fill="#222"/><circle cx="5" cy="5" r="2.5" fill="none" stroke="#fff" stroke-width="0.8"/></svg>
    www.marwick.com.au
  </div>
  <div class="brand">
    <span class="brand-mark"></span>
    <span class="brand-name">Marwick Global Logistics</span>
  </div>
  <div class="rule"></div>
  <div class="tagline">GLOBAL LOGISTICS</div>
</section>

</body>
</html>
```